Cloud Software Services Business Needs New Website Design

Our client is looking for a really modern design for their cloud services company. We have a logo, but apart from that, if you read the brief fully and digest the wireframes, we hope you will come up with a really amazing end product.

The design of the website should be professional and trustworthy, it is there to inspire confidence in the services and softwares, as well as emphasising the track record of RMV and relative knowledge and competencies.

Given all the cloud-related communications in the messaging on the site, we will need this in either the imagery or icons in the site so that we can connect the messaging with the service offering.

The brand, being black, gives full range for the designer to present a palette that serves the brand, not forgetting the audience are generally IT decision-makers.

Target Market(s)

Managers and Directors Responsible for IT/Cloud Infrastructure

Industry/Entity Type

IT Technology

Number of Pages Required

5+ page

Font styles to use
Sans Serif

Requirements
Must have
• Initial designs which match the brief and wireframes, focus on the homepage and the winning designer will need to supply the internal pages for the website.
Nice to have
• Clearly considered professional website designs, with consistent design work and branding. If choosing stock imagery, then from PixHarbor Basics please.
Should not have
• Not too much colour, or too consumer/youthful.

```html
<!DOCTYPE html>
<html lang="en">
<head>
<meta charset="utf-8">
<title>RMV – Cloud Services</title>
<link href="https://fonts.googleapis.com/css2?family=Montserrat:ital,wght@0,400;0,500;0,600;0,700;0,800;1,500&display=swap" rel="stylesheet">
<style>
:root{
  --navy:#0b1a3a;
  --deep:#06102a;
  --blue:#1672c8;
  --bright:#1f8fe8;
  --sky:#dbeefc;
  --orange:#f58220;
  --ink:#1b1f2a;
  --text:#4a4f5c;
  --grey:#f1f2f4;
  --logo-grey:#8a8d94;
  --white:#ffffff;
  --footer:#0d1322;
}
*{margin:0;padding:0;box-sizing:border-box}
html,body{width:1200px;height:5172px;overflow:hidden}
body{font-family:"Montserrat",sans-serif;color:var(--text);background:var(--white);position:relative}
.sec{position:absolute;left:0;width:1200px}
.btn{display:inline-block;background:var(--orange);color:var(--white);font-weight:700;font-size:15px;letter-spacing:.5px;padding:14px 30px;text-transform:uppercase;white-space:nowrap}
h2{font-family:"Montserrat",sans-serif;font-weight:600;color:var(--ink);text-transform:uppercase}
h2 strong{color:var(--blue);font-weight:800}

/* top bar */
.topbar{top:0;height:40px;background:#f7f8fa;font-size:13px;color:var(--text);display:flex;justify-content:space-between;align-items:center;padding:0 60px}
.topbar .contact span{margin-right:26px;display:inline-flex;align-items:center;gap:7px}
.topbar .ico{width:14px;height:14px;background:var(--blue);border-radius:2px;display:inline-block}
.topbar .links{color:var(--blue);font-weight:500;font-size:12px}
.topbar .links span{margin-left:12px}

/* header */
.header{top:40px;height:110px;display:flex;align-items:center;justify-content:space-between;padding:0 60px}
.logo{font-weight:700;font-size:46px;color:var(--ink);letter-spacing:1px}
.nav span{margin-left:40px;font-size:15px;font-weight:700;color:var(--ink)}
.nav .active{color:var(--orange)}

/* hero */
.hero{top:150px;height:650px;overflow:hidden}
.hero-bg{position:absolute;inset:0;background:radial-gradient(circle at 72% 40%,#5aa8e6 0%,#1c4c91 25%,#0b1f4b 55%,var(--deep) 100%)}
.hero h1{position:absolute;left:60px;top:170px;color:var(--white);font-size:60px;font-weight:800;line-height:1.1;text-transform:uppercase}
.hero-wave{position:absolute;left:0;bottom:0;width:1200px;height:260px}
.lining{position:absolute;left:90px;top:505px;display:flex;align-items:center;gap:46px;color:var(--white);font-size:15px;font-weight:600}
.lining .title{font-size:20px;font-weight:800;margin-right:20px}
.lining .item{display:flex;align-items:center;gap:10px}
.tick{width:24px;height:24px;border:2px solid var(--white);border-radius:50%;display:inline-flex;align-items:center;justify-content:center}

/* intro */
.intro{top:800px;height:580px;text-align:center}
.intro h2{font-size:34px;line-height:1.25;margin-top:26px}
.intro p{font-size:16px;line-height:1.6;max-width:1000px;margin:12px auto 0}
.intro .lead{font-weight:700;color:var(--ink);font-size:18px;margin-top:28px}
.promises{display:flex;justify-content:center;gap:110px;margin-top:26px}
.promise{width:260px}
.num{width:100px;height:100px;border-radius:50%;background:var(--sky);margin:0 auto 14px;display:flex;align-items:center;justify-content:center;font-size:54px;font-style:italic;font-weight:500;color:var(--blue)}
.promise p{font-size:14px;margin:0;line-height:1.5}
.cta-line{margin-top:26px!important;font-weight:700;color:var(--ink);font-size:17px!important}
.cta-line .btn{margin-left:18px;padding:11px 28px;font-size:14px}

/* tools */
.tools{top:1380px;height:760px;overflow:hidden}
.tools-bg{position:absolute;inset:0;background:linear-gradient(160deg,#3a4250 0%,#1c2230 45%,#0a0f1c 100%)}
.tools .wave{position:absolute;left:0;width:1200px}
.tools-text{position:absolute;top:395px;width:1200px;text-align:center;color:var(--white)}
.tools-text h3{font-size:24px;font-weight:800;text-transform:uppercase}
.tools-text h2{color:var(--white);font-size:38px;font-weight:800;margin-top:8px}
.tools-text .btn{margin-top:36px;padding:12px 30px;font-size:14px}

/* move card */
.move{top:2065px;left:75px;width:1050px;height:375px;background:var(--white);box-shadow:0 6px 30px rgba(0,0,0,.15);text-align:center;padding-top:34px}
.move h2{font-size:32px}
.providers{display:flex;justify-content:center;gap:220px;margin-top:32px}
.provider .mark{width:96px;height:96px;border-radius:50%;background:var(--sky);margin:0 auto}
.provider .name{margin-top:14px;font-weight:700;font-size:18px;color:var(--blue);text-transform:uppercase}
.provider .btn{margin-top:14px;padding:9px 22px;font-size:13px}

/* advice */
.advice{top:2445px;height:320px;text-align:center}
.advice h2{font-size:30px;margin-top:18px}
.advice p{font-size:16px;line-height:1.7;max-width:1060px;margin:16px auto 0}

/* savings */
.savings{top:2772px;height:460px;background:linear-gradient(120deg,#0f3e95 0%,#1a5fc2 50%,#0c2f78 100%);overflow:hidden}
.badge{position:absolute;left:75px;top:80px;width:270px;height:270px;transform:rotate(-8deg)}
.badge-shape{position:absolute;inset:0;background:linear-gradient(135deg,#2a9cf0,#0d5ec0);box-shadow:10px 10px 30px rgba(0,0,0,.35)}
.badge-text{position:absolute;inset:0;display:flex;flex-direction:column;align-items:center;justify-content:center;color:var(--white);font-weight:800}
.badge-text .pct{font-size:92px;line-height:1}
.badge-text .word{font-size:26px;letter-spacing:2px}
.save-copy{position:absolute;left:520px;top:90px;width:630px;color:var(--white)}
.save-copy h2{color:var(--white);font-size:28px;font-weight:600;white-space:nowrap}
.save-copy h2 strong{color:var(--white)}
.save-copy p{font-size:15px;line-height:1.7;margin-top:14px}
.save-copy .btn{margin-top:30px;padding:11px 28px;font-size:13px}

/* start */
.start{top:3232px;height:340px;text-align:center}
.start h2{font-size:34px;margin-top:76px}
.start p{font-size:16px;line-height:1.7;max-width:820px;margin:20px auto 0}
.start .btns{margin-top:30px}
.start .btn{margin:0 10px;padding:13px 30px;font-size:14px}

/* blog */
.blog{top:3560px;height:640px;background:var(--grey);overflow:hidden}
.blog .wave{position:absolute;left:0;width:1200px}
.blog h2{position:absolute;top:58px;width:1200px;text-align:center;font-size:30px;font-weight:700}
.posts{position:absolute;top:112px;left:60px;display:flex;gap:27px}
.post{width:250px}
.post .thumb{height:170px}
.post h4{margin-top:14px;font-size:18px;font-weight:600;color:var(--ink);line-height:1.35}

/* trusted */
.trusted{top:4200px;height:360px;text-align:center}
.trusted h2{font-size:30px;font-weight:700;margin-top:68px}
.clients{margin:34px auto 0;width:1100px;display:flex;justify-content:space-around;align-items:center}
.clients.row2{margin-top:34px;width:1060px}
.client{font-size:26px;font-weight:700;color:var(--logo-grey);white-space:nowrap}

/* footer */
.footer{top:4560px;height:612px;background:var(--footer);color:#c9ccd4;overflow:hidden}
.cols{position:absolute;left:60px;top:42px;display:flex;gap:0}
.col{width:270px}
.col h5{color:var(--white);font-size:15px;font-weight:800;text-transform:uppercase;margin-bottom:12px}
.col li{list-style:none;font-size:13px;line-height:1.9}
.col h5.later{margin-top:22px}
.seals{display:flex;gap:20px;margin-top:24px}
.seal{width:74px;height:74px;border-radius:50%;background:#e8eaef}
.legal{position:absolute;left:0;bottom:0;width:1200px;height:60px;border-top:1px solid #232a3b;display:flex;justify-content:space-between;align-items:center;padding:0 60px;font-size:12px;color:#8e93a0}
.legal span span{margin-left:16px}
</style>
</head>
<body>

<div class="sec topbar">
  <div class="contact">
    <span><i class="ico"></i>01632 960 418</span>
    <span><i class="ico"></i>Email Us</span>
    <span><i class="ico"></i>NetConnect</span>
  </div>
  <div class="links"><span>PARTNERS</span> | <span>BLOG</span> | <span>ABOUT US</span> | <span>CONTACT US</span></div>
</div>

<header class="sec header">
  <div class="logo">rmv</div>
  <nav class="nav"><span class="active">HOME</span><span>CLOUD</span><span>SOFTWARE</span><span>SERVICES</span></nav>
</header>

<section class="sec hero">
  <div class="hero-bg" role="img" aria-label="Hand reaching toward a glowing cloud network over a dark blue city at night"></div>
  <h1>Opreating under<br>a cloud?</h1>
  <svg class="hero-wave" viewBox="0 0 1200 260" preserveAspectRatio="none">
    <path d="M0 60 C300 90 520 170 760 140 C960 115 1090 60 1200 30 L1200 260 L0 260 Z" fill="#0a1a44" opacity=".85"/>
    <path d="M0 200 C260 255 520 255 760 220 C960 190 1100 165 1200 175 L1200 260 L0 260 Z" fill="#ffffff"/>
    <path d="M0 200 C260 255 520 255 760 220 C960 190 1100 165 1200 175" fill="none" stroke="#1f8fe8" stroke-width="6"/>
  </svg>
  <div class="lining">
    <span class="title">THERE'S A SILVER LINING</span>
    <span class="item"><span class="tick"><svg width="12" height="12" viewBox="0 0 12 12"><path d="M2 6l3 3 5-6" stroke="#fff" stroke-width="2" fill="none"/></svg></span>REDUCING COSTS</span>
    <span class="item"><span class="tick"><svg width="12" height="12" viewBox="0 0 12 12"><path d="M2 6l3 3 5-6" stroke="#fff" stroke-width="2" fill="none"/></svg></span>MIGRATION</span>
    <span class="item"><span class="tick"><svg width="12" height="12" viewBox="0 0 12 12"><path d="M2 6l3 3 5-6" stroke="#fff" stroke-width="2" fill="none"/></svg></span>WORK WITH US</span>
  </div>
</section>

<section class="sec intro">
  <h2>Did the promise of <strong>cloud computing<br>happen for you?</strong></h2>
  <p>We didn't think so! You're not alone. There are many companies just like you who believed in the promise of cloud computing but are now shocked by it.</p>
  <p>But there is a silver lining, which is that RMV have built a business around helping companies improve their cloud efficiencies, reduce costs and simplify their operations as a result.</p>
  <p class="lead">It can be summarised in three promises RMV makes to every client or partner:</p>
  <div class="promises">
    <div class="promise"><div class="num">1</div><p>You can reduce cloud costs, without needing to move supplier.</p></div>
    <div class="promise"><div class="num">2</div><p>You can migrate from one cloud to another more easily.</p></div>
    <div class="promise"><div class="num">3</div><p>You can simplify your cloud management and choose your favoured provider.</p></div>
  </div>
  <p class="cta-line">If you already know or want to talk to us just call 01632 960 418 &nbsp;or <span class="btn">Send an email</span></p>
</section>

<section class="sec tools">
  <div class="tools-bg" role="img" aria-label="Team of people around a meeting table with laptops, seen from above"></div>
  <svg class="wave" style="top:0;height:120px" viewBox="0 0 1200 120" preserveAspectRatio="none">
    <path d="M0 0 L1200 0 L1200 30 C900 110 500 110 0 50 Z" fill="#ffffff"/>
    <path d="M0 50 C500 110 900 110 1200 30" fill="none" stroke="#1672c8" stroke-width="10"/>
  </svg>
  <div class="tools-text">
    <h3>Your cloud your tools</h3>
    <h2>A suite of software to simplify deployment</h2>
    <span class="btn">Cloud software</span>
  </div>
  <svg class="wave" style="bottom:0;height:140px" viewBox="0 0 1200 140" preserveAspectRatio="none">
    <path d="M0 60 C400 140 800 130 1200 40 L1200 140 L0 140 Z" fill="#ffffff"/>
    <path d="M0 60 C400 140 800 130 1200 40" fill="none" stroke="#1672c8" stroke-width="10"/>
  </svg>
</section>

<section class="sec move">
  <h2>How hard is it to <strong>move your cloud?</strong></h2>
  <div class="providers">
    <div class="provider"><div class="mark"></div><div class="name">Skyforge</div><span class="btn">View more</span></div>
    <div class="provider"><div class="mark"></div><div class="name">Bluevault</div><span class="btn">View more</span></div>
    <div class="provider"><div class="mark"></div><div class="name">Orbitra</div><span class="btn">View more</span></div>
  </div>
</section>

<section class="sec advice">
  <h2>Knowledgeable independent advice matters</h2>
  <p>Traditionally, the balance of power lies with your host, who has no interest in you moving to another platform. It may also be that your cloud supplier is a linked to your IT firm, developer or even staff preferences – and in some cases they will specialise in only one of these suppliers.</p>
  <p>It's time to break free. RMV equips companies, resellers and consultants with the power to choose, to negotiate, to move. We can do this for you.</p>
</section>

<section class="sec savings">
  <div class="badge">
    <div class="badge-shape"></div>
    <div class="badge-text"><span class="pct">20%</span><span class="word">CHEAPER</span></div>
  </div>
  <div class="save-copy">
    <h2>Make your <strong>cloud costs evaporate</strong></h2>
    <p>As cloud costs continue to escalate, and as you suddenly hit new tiers of spend, you may feel helpless in the face of rising costs. However, even taking the cost of moving into account, RMV has estimated the average client will save 20% of spend on their cloud by using us to find the best solution and help you to move there.</p>
    <span class="btn">Get case studies</span>
  </div>
</section>

<section class="sec start">
  <h2>Let's <strong>get started</strong></h2>
  <p>If you would like to speak to a friendly and helpful member of our team, ask questions, discuss options or to help with anything on your mind, please get in touch.</p>
  <div class="btns"><span class="btn">Call 01632 960 418</span><span class="btn">Send an email</span></div>
</section>

<section class="sec blog">
  <svg class="wave" style="top:0;height:70px" viewBox="0 0 1200 70" preserveAspectRatio="none">
    <path d="M0 0 L1200 0 L1200 10 C800 70 400 70 0 20 Z" fill="#ffffff"/>
    <path d="M0 20 C400 70 800 70 1200 10" fill="none" stroke="#1672c8" stroke-width="8"/>
  </svg>
  <h2>RMV <strong>Blog</strong></h2>
  <div class="posts">
    <div class="post"><div class="thumb" role="img" aria-label="Blue digital cloud network graphic" style="background:linear-gradient(135deg,#0b2a6b,#2a8ff0)"></div><h4>Neque porro quisquam est qui dolore</h4></div>
    <div class="post"><div class="thumb" role="img" aria-label="Hands holding a glowing cloud icon" style="background:linear-gradient(135deg,#1b2c4a,#7fb8e8)"></div><h4>Neque porro quisquam est qui dolore</h4></div>
    <div class="post"><div class="thumb" role="img" aria-label="Server room lit in blue" style="background:linear-gradient(135deg,#061436,#1f5fb8)"></div><h4>Neque porro quisquam est qui dolore</h4></div>
    <div class="post"><div class="thumb" role="img" aria-label="Glowing cloud above a circuit board" style="background:linear-gradient(135deg,#0a2a66,#58b2f2)"></div><h4>Neque porro quisquam est qui dolore</h4></div>
  </div>
  <svg class="wave" style="bottom:0;height:110px" viewBox="0 0 1200 110" preserveAspectRatio="none">
    <path d="M0 40 C400 110 800 110 1200 20 L1200 110 L0 110 Z" fill="#ffffff"/>
    <path d="M0 40 C400 110 800 110 1200 20" fill="none" stroke="#1672c8" stroke-width="8"/>
  </svg>
</section>

<section class="sec trusted">
  <h2>Trusted <strong>by</strong></h2>
  <div class="clients">
    <span class="client">Datavane</span><span class="client">TRX</span><span class="client">Larchmont Capital</span><span class="client">FERN</span><span class="client">NOA</span>
  </div>
  <div class="clients row2">
    <span class="client">Billwell</span><span class="client">BrightlineAction</span><span class="client">QUILLMARK</span><span class="client">HARLOW &amp; HARLOW</span>
  </div>
</section>

<footer class="sec footer">
  <div class="cols">
    <div class="col"><h5>Cloud services</h5><ul><li>Skyforge</li><li>Bluevault</li><li>Orbitra</li><li>Quorra</li><li>Kestrel</li><li>Deepwell</li><li>Others</li><li>Private Cloud</li></ul></div>
    <div class="col"><h5>Services</h5><ul><li>Cloud Cost Review</li><li>Migration Planning</li><li>Migration Execution</li><li>Security &amp; Compliance</li></ul><h5 class="later">Software</h5><ul><li>Skylatch</li><li>OmniDesk</li></ul></div>
    <div class="col"><h5>About RMV</h5><ul><li>Blog</li><li>Partners</li><li>About Us</li><li>Contact Us</li></ul><h5 class="later">Services</h5><ul><li>Cloud Cost Review</li><li>Migration Planning</li><li>Migration Execution</li><li>Security &amp; Compliance</li></ul></div>
    <div class="col"><h5>Connect</h5><ul><li>Harrow House Mill Lane</li><li>Westbrook WB4 2QT</li><li>England</li><li>&nbsp;</li><li>01632 960 418</li><li>Email Us</li><li>NetConnect</li></ul><div class="seals"><div class="seal"></div><div class="seal"></div></div></div>
  </div>
  <div class="legal"><span>© 2022 RMV Computing Group Limited. All rights reserved.</span><span><span>Sitemap</span><span>Terms of Use</span><span>Privacy Policy</span><span>Contact Us</span></span></div>
</footer>

</body>
</html>
```